General Contractor Website Design

We are working with a General Contractor in California that specializes in building custom kitchens, baths, and homes for high-end clients.

Here are some websites for inspiration:
https://morvelstudio.example/
https://ridgelanebuildworks.example
https://www.framequill.example
https://www.nestiva.example
https://www.tzdwell.example
https://rplresidences.example

Thank you for taking the time to consider designing a website for us. We are web developers based in Stockton, CA, USA. Most of our projects go through the same process. Understanding this process may help you win a project with us. We custom-code all of our websites in-house. We don’t have any requirements as to what tools you use for your design, but we ask that you follow these guidelines.

IMAGES:
If you use any images or icons in the design, we ask that you have a link to the asset so we can purchase the image/icon. Most of the designs we submit do not have the customer’s images on them unless they have some great images. Be creative; show us the feeling you are trying to portray with your image choices. Use any royalty-free site you choose. We subscribe to Velqor and mainly use their images, but we can purchase images outside of Velqor. PLEASE NOTE: we will not submit designs to clients with watermarks on the images.

FONTS:
We ask that you identify the fonts you’re using in the design. This can be done in a message if you want. We typically use Google Fonts and Velqor Fonts.

CONTENT:
We're always open to different content and ideas. We often submit designs with stock images so the client can see our vision. We typically take pictures after the website launch to use their images with our vision. Lorem Ipsum is fine for paragraphs, but we ask that you make the Headers with correct English. We want to be able to show the vision and identify the sections of the website.

INSPIRATION:
We typically add a couple of links in the brief of websites we like to help you get started in your design.

REVISIONS:
We do not often ask for revisions of the designs unless we see something in the design that may not appeal to the client. If there are slight changes that we want to make, we do that in the development process.

FEEDBACK:
We rarely give feedback on designs during the design process. We are working on many website projects and do not have the time to provide feedback. We usually respond if your request is well thought out and asks specific questions, but a note asking “feedback, please” usually goes unanswered.

```html
<!DOCTYPE html>
<html lang="en">
<head>
<meta charset="utf-8">
<title>Hollin Builders – Custom Homes, Kitchens and Baths</title>
<link rel="stylesheet" href="https://fonts.googleapis.com/css2?family=Roboto:wght@300;400;500&display=swap">
<style>
:root{
  --red:#e3202b;
  --black:#000;
  --white:#fff;
  --ink:#222;
  --muted:#666;
  --grey-light:#f1f1f3;
  --grey-mid:#dcdde0;
  --text-dim:#8a8a8a;
}
*{box-sizing:border-box;margin:0;padding:0}
html,body{width:1200px;height:4029px;overflow:hidden;background:var(--white)}
body{position:relative;font-family:'Roboto',Arial,sans-serif;color:var(--ink)}
.abs{position:absolute}
a{color:inherit;text-decoration:none}

/* hero */
.hero{left:0;top:0;width:1200px;height:677px;
  background:linear-gradient(180deg,#5d7d93 0%,#8aa2b2 18%,#b9c2c9 45%,#cfd3d6 70%,#e3e4e5 100%);
  box-shadow:0 2px 4px rgba(0,0,0,.25)}
.hero-bar{left:0;top:41px;width:1200px;height:76px;background:rgba(60,75,90,.35)}
.brand{display:flex;align-items:center;gap:10px;font-weight:500;letter-spacing:3px;font-size:22px;line-height:26px;color:var(--red);text-transform:uppercase;white-space:nowrap}
.brand-mark{width:22px;height:22px;background:var(--red);flex:none}
.hero-brand{left:44px;top:66px}
.main-nav{left:684px;top:72px;display:flex;font-size:15px;line-height:16px;color:var(--white)}
.main-nav a{padding:0 12px;border-left:1px solid rgba(255,255,255,.7)}
.main-nav a:first-child{border-left:none;color:var(--red)}
.hero-title{left:0;width:1200px;top:178px;text-align:center;color:var(--white);font-size:50px;font-weight:400;line-height:83px}
.hero-title span{color:var(--red)}
.hero-sub{left:0;width:1200px;top:412px;text-align:center;color:var(--white);font-size:31px;font-weight:300}
.hero-rule{top:438px;width:62px;height:3px;background:var(--red)}
.hero-link{top:568px;font-size:21px;color:var(--red);text-decoration:underline;display:flex;align-items:center;gap:10px}
.hero-link::before,.hero-link::after{content:"";width:6px;height:6px;border-radius:50%;background:var(--white)}

/* headings */
.section-title{left:0;width:1200px;text-align:center;color:var(--red);font-size:30px;font-weight:400}
.caps{font-size:23px;text-transform:uppercase}

/* latest work carousel */
.photo{background:#ccc}
.shadowed{box-shadow:0 2px 6px rgba(0,0,0,.3)}
.arrow{top:1040px}

/* about */
.about{left:0;top:1444px;width:1200px;height:332px;background:linear-gradient(180deg,var(--grey-mid),var(--grey-light) 60%,#f7f7f8);border-bottom:2px solid #cfcfd2}
.body-copy{left:120px;width:960px;text-align:center;font-size:13.5px;line-height:22px;color:var(--muted);font-weight:300}

/* featured */
.band-dark{left:0;width:1200px;background:var(--black)}
.feature-label{font-size:19px;color:var(--red);text-transform:uppercase;display:flex;align-items:center;gap:8px}
.project-name{font-size:16px;font-weight:400}
.dark .project-name{color:var(--white)}
.feature-copy{width:330px;font-size:11.5px;line-height:15px;color:var(--text-dim);font-weight:300}
.feature-copy p{margin-bottom:14px}
.details{font-size:12px;color:var(--red);display:flex;align-items:center;gap:8px}

/* mission */
.btn{left:501px;top:3695px;width:197px;height:38px;background:var(--red);color:var(--white);font-size:18px;display:flex;align-items:center;justify-content:center}

/* footer */
.footer-rule{left:0;top:3860px;width:1200px;height:1px;background:#ddd}
.footer-brand{left:47px;top:3902px;font-size:20px}
.social{top:3966px;width:22px;height:22px;border-radius:50%;background:#777}
.foot-nav{left:463px;top:3900px;display:flex;font-size:15px;color:var(--black)}
.foot-nav a{padding:0 7px;border-left:1px solid #555;line-height:15px}
.foot-nav a:first-child{border-left:none;padding-left:0}
.legal{left:0;width:1200px;top:3943px;text-align:center;font-size:11px;color:var(--muted)}
.contact-title{left:912px;top:3896px;font-size:18px;font-weight:400;color:var(--black)}
.contact-line{left:912px;font-size:11.5px;color:var(--muted);display:flex;align-items:center;gap:10px}
.copyright{left:0;width:1200px;top:4006px;text-align:center;font-size:8px;color:#bbb}
</style>
</head>
<body>

<header class="hero abs" role="img" aria-label="Photo of a modern white two-storey home with glass balconies"></header>
<div class="hero-bar abs"></div>
<div class="brand hero-brand abs"><span class="brand-mark"></span>Hollin Builders</div>
<nav class="main-nav abs">
  <a href="#">Home</a><a href="#">Portfolio</a><a href="#">Services</a><a href="#">About Us</a><a href="#">Contact Us</a>
</nav>
<h1 class="hero-title abs"><span>The finest</span> home in the world is<br>built by hand.</h1>
<div class="hero-rule abs" style="left:321px"></div>
<p class="hero-sub abs">turn your dream into reality</p>
<div class="hero-rule abs" style="left:817px"></div>
<a class="hero-link abs" style="left:107px" href="#">Portfolio</a>
<a class="hero-link abs" style="left:958px" href="#">Contact Us</a>

<h2 class="section-title abs" style="top:772px">Our Latest Work</h2>
<svg class="arrow abs" style="left:28px" width="26" height="44" viewBox="0 0 26 44"><path d="M22 2 4 22l18 20" fill="none" stroke="#555" stroke-width="2.5"/></svg>
<div class="photo shadowed abs" style="left:77px;top:814px;width:342px;height:453px;background:linear-gradient(135deg,#2f7fd6,#8fb6e4 45%,#e8e8e8 55%,#9a9a9a)" role="img" aria-label="White modern building with balcony against blue sky"></div>
<div class="photo shadowed abs" style="left:429px;top:865px;width:342px;height:452px;background:linear-gradient(180deg,#6e8aa0,#2a2f33 45%,#1c1c1c 75%,#5a5a5a)" role="img" aria-label="Black modern house lit at dusk among trees"></div>
<div class="photo shadowed abs" style="left:779px;top:917px;width:343px;height:455px;background:linear-gradient(180deg,#9fb7a0,#5f7d3e 45%,#2f8a80 70%,#d2d6da)" role="img" aria-label="Garden pool with palm trees and green wall"></div>
<svg class="arrow abs" style="left:1146px" width="26" height="44" viewBox="0 0 26 44"><path d="M4 2l18 20L4 42" fill="none" stroke="#555" stroke-width="2.5"/></svg>

<section class="about abs" aria-labelledby="about-title"></section>
<h2 id="about-title" class="section-title caps abs" style="top:1490px">About Us</h2>
<p class="body-copy abs" style="top:1555px">felis, tempor non diam nisi viverra eu nulla, Nullam quam libero, elementum amet, convallis. luctus sodales. adipiscing quam placerat non tincidunt eget nec tempor nisl. vitae vitae ex tincidunt nibh quis sed nec Nam nec consectetur elit ex. nec placerat elit Ut Nunc sit elit ex Nunc eget Nunc elit. vitae vitae ac eget urna. quis Morbi Lorem viverra leo. viverra sapien nec eget tincidunt ex. gravida Nam tincidunt Sed nisl. luctus orci dignissim, libero, turpis tincidunt</p>
<p class="body-copy abs" style="top:1654px">felis, tempor non diam nisi viverra eu nulla, Nullam quam libero, elementum amet, convallis. luctus sodales. adipiscing quam placerat non tincidunt eget nec tempor nisl. vitae vitae ex tincidunt nibh quis sed nec Nam nec consectetur elit ex. nec placerat elit Ut Nunc sit elit ex Nunc eget Nunc elit. vitae vitae ac eget urna. quis Morbi Lorem viverra leo. viverra sapien nec eget tincidunt ex. gravida Nam tincidunt Sed nisl. luctus orci dignissim, libero, turpis tincidunt</p>

<h2 class="section-title abs" style="top:1847px;font-size:23px">Featured Work</h2>

<!-- homes -->
<section class="band-dark dark abs" style="top:1918px;height:454px"></section>
<div class="dark">
  <div class="feature-label abs" style="left:59px;top:1953px">Homes <svg width="16" height="14" viewBox="0 0 16 14"><path d="M1 7h13M8 1l6 6-6 6" fill="none" stroke="#e3202b" stroke-width="1.8"/></svg></div>
  <h3 class="project-name abs" style="left:59px;top:2027px">Project Name</h3>
  <div class="feature-copy abs" style="left:59px;top:2068px">
    <p>felis, tempor non diam nisi viverra eu nulla, Nullam quam libero, elementum amet, convallis. luctus sodales. adipiscing quam placerat non tincidunt eget nec</p>
    <p>tempor nisl. vitae vitae ex tincidunt nibh quis sed nec Nam nec consectetur elit ex. nec placerat elit Ut Nunc sit elit ex Nunc eget Nunc elit. vitae vitae ac</p>
    <p>eget urna. quis Morbi Lorem viverra leo. viverra sapien nec eget tincidunt ex. gravida Nam tincidunt Sed nisl. luctus orci dignissim, libero, turpis tincidunt</p>
  </div>
  <a class="details abs" style="left:59px;top:2294px" href="#">Project Details <span>»</span></a>
</div>
<div class="photo abs" style="left:480px;top:1953px;width:341px;height:383px;background:linear-gradient(180deg,#6b4a30,#e9e4dc 30%,#f3f1ec 70%,#9b6c45)" role="img" aria-label="Living room with wooden beams and arched windows"></div>
<div class="photo abs" style="left:840px;top:1953px;width:299px;height:183px;background:linear-gradient(180deg,#9a6a45,#ece8e2 30%,#f4f2ee)" role="img" aria-label="Bright dining nook with wall art"></div>
<div class="photo abs" style="left:840px;top:2154px;width:299px;height:182px;background:linear-gradient(180deg,#3d3d3f,#6a6a6c 50%,#e2e0dc)" role="img" aria-label="Dark bedroom with upholstered bed"></div>

<!-- kitchens -->
<div class="photo abs" style="left:59px;top:2406px;width:299px;height:384px;background:linear-gradient(180deg,#f2f2f2,#b58454 40%,#1b1b1b 75%,#d9d9d9)" role="img" aria-label="Kitchen with wood cabinets and black island"></div>
<div class="photo abs" style="left:377px;top:2406px;width:294px;height:174px;background:linear-gradient(90deg,#e5e5e5,#2a2623 30%,#a67a4f 70%,#3a3a3a)" role="img" aria-label="Kitchen shelving with wood counter and bar stool"></div>
<div class="photo abs" style="left:377px;top:2599px;width:138px;height:191px;background:linear-gradient(180deg,#8a5b34,#c98c4d 50%,#5a2a18)" role="img" aria-label="Warm wood kitchen with hardwood floor"></div>
<div class="photo abs" style="left:532px;top:2599px;width:139px;height:191px;background:linear-gradient(180deg,#9b7352,#3a3634 50%,#dedede)" role="img" aria-label="Kitchen with dark built-in ovens"></div>
<div class="feature-label abs" style="left:784px;top:2406px">Kitchens <svg width="16" height="14" viewBox="0 0 16 14"><path d="M1 7h13M8 1l6 6-6 6" fill="none" stroke="#e3202b" stroke-width="1.8"/></svg></div>
<h3 class="project-name abs" style="left:784px;top:2481px">Project Name</h3>
<div class="feature-copy abs" style="left:780px;top:2522px">
  <p>felis, tempor non diam nisi viverra eu nulla, Nullam quam libero, elementum amet, convallis. luctus sodales. adipiscing quam placerat non tincidunt eget nec</p>
  <p>tempor nisl. vitae vitae ex tincidunt nibh quis sed nec Nam nec consectetur elit ex. nec placerat elit Ut Nunc sit elit ex Nunc eget Nunc elit. vitae vitae ac</p>
  <p>eget urna. quis Morbi Lorem viverra leo. viverra sapien nec eget tincidunt ex. gravida Nam tincidunt Sed nisl. luctus orci dignissim, libero, turpis tincidunt</p>
</div>
<a class="details abs" style="left:784px;top:2750px" href="#">Project Details <span>»</span></a>

<!-- baths -->
<section class="band-dark dark abs" style="top:2826px;height:452px"></section>
<div class="dark">
  <div class="feature-label abs" style="left:59px;top:2862px">Baths <svg width="16" height="14" viewBox="0 0 16 14"><path d="M1 7h13M8 1l6 6-6 6" fill="none" stroke="#e3202b" stroke-width="1.8"/></svg></div>
  <h3 class="project-name abs" style="left:59px;top:2935px">Project Name</h3>
  <div class="feature-copy abs" style="left:57px;top:2976px">
    <p>felis, tempor non diam nisi viverra eu nulla, Nullam quam libero, elementum amet, convallis. luctus sodales. adipiscing quam placerat non tincidunt eget nec</p>
    <p>tempor nisl. vitae vitae ex tincidunt nibh quis sed nec Nam nec consectetur elit ex. nec placerat elit Ut Nunc sit elit ex Nunc eget Nunc elit. vitae vitae ac</p>
    <p>eget urna. quis Morbi Lorem viverra leo. viverra sapien nec eget tincidunt ex. gravida Nam tincidunt Sed nisl. luctus orci dignissim, libero, turpis tincidunt</p>
  </div>
  <a class="details abs" style="left:59px;top:3203px" href="#">Project Details <span>»</span></a>
</div>
<div class="photo abs" style="left:480px;top:2862px;width:401px;height:178px;background:linear-gradient(180deg,#d8dcd8,#8d9590 50%,#e9e9e7)" role="img" aria-label="Bathroom with glass shower and soaking tub"></div>
<div class="photo abs" style="left:898px;top:2862px;width:243px;height:178px;background:linear-gradient(180deg,#6a6c6e,#3e4042 50%,#b9bbbd)" role="img" aria-label="Dark grey bathroom with freestanding tub"></div>
<div class="photo abs" style="left:480px;top:3057px;width:146px;height:186px;background:linear-gradient(180deg,#5c5f60,#b3b5b5 50%,#e2e2e2)" role="img" aria-label="Bathroom window and white tub"></div>
<div class="photo abs" style="left:643px;top:3057px;width:498px;height:186px;background:linear-gradient(90deg,#9c9c9c,#c8c8c8 40%,#efefef 70%,#b0b0b0)" role="img" aria-label="Grey marble bathroom with black basin and round mirror"></div>

<h2 class="section-title caps abs" style="top:3346px">Our Mission</h2>
<p class="body-copy abs" style="top:3420px">felis, tempor non diam nisi viverra eu nulla, Nullam quam libero, elementum amet, convallis. luctus sodales. adipiscing quam placerat non tincidunt eget nec tempor nisl. vitae vitae ex tincidunt nibh quis sed nec Nam nec consectetur elit ex. nec placerat elit Ut Nunc sit elit ex Nunc eget Nunc elit. vitae vitae ac eget urna. quis Morbi Lorem viverra leo. viverra sapien nec eget tincidunt ex. gravida Nam tincidunt Sed nisl. luctus orci dignissim, libero, turpis tincidunt</p>
<p class="body-copy abs" style="top:3520px;left:95px;width:1010px">felis, tempor non diam nisi viverra eu nulla, Nullam quam libero, elementum amet, convallis. luctus sodales. adipiscing quam placerat non tincidunt eget nec tempor nisl. vitae vitae ex tincidunt nibh quis sed nec Nam nec consectetur elit ex. nec placerat elit Ut Nunc sit elit ex Nunc eget Nunc elit. vitae vitae ac eget urna. quis Morbi Lorem viverra leo. viverra sapien nec eget tincidunt ex. gravida Nam tincidunt Sed nisl. luctus orci dignissim, libero, turpis tincidunt</p>
<a class="btn abs" href="#">Contact Us</a>

<footer class="footer">
  <div class="footer-rule abs"></div>
  <div class="brand footer-brand abs"><span class="brand-mark"></span>Hollin Builders</div>
  <span class="social abs" style="left:114px" aria-label="Social link"></span>
  <span class="social abs" style="left:147px" aria-label="Social link"></span>
  <span class="social abs" style="left:180px" aria-label="Social link"></span>
  <nav class="foot-nav abs"><a href="#">Home</a><a href="#">Portfolio</a><a href="#">Services</a><a href="#">About us</a></nav>
  <p class="legal abs">Terms of service | Privacy Policy</p>
  <h4 class="contact-title abs">Get in touch</h4>
  <p class="contact-line abs" style="top:3932px"><svg width="9" height="12" viewBox="0 0 9 12"><path d="M4.5 0A4.5 4.5 0 0 0 0 4.5C0 8 4.5 12 4.5 12S9 8 9 4.5A4.5 4.5 0 0 0 4.5 0Zm0 6.3a1.8 1.8 0 1 1 0-3.6 1.8 1.8 0 0 1 0 3.6Z" fill="#777"/></svg>luctus orci dignissim, libero, turpis tincidunt</p>
  <p class="contact-line abs" style="top:3956px"><svg width="10" height="10" viewBox="0 0 10 10"><path d="M2 0l2 2.5-1.2 1.3a6 6 0 0 0 3.4 3.4L7.5 6 10 8 8.5 10C4 10 0 6 0 1.5Z" fill="#777"/></svg>+123 555 0198</p>
  <p class="contact-line abs" style="top:3979px"><svg width="11" height="8" viewBox="0 0 11 8"><rect width="11" height="8" fill="#777"/><path d="M0 0l5.5 4.5L11 0" fill="none" stroke="#fff"/></svg>dana.reyes@example.com</p>
  <p class="copyright abs">© Copyright 2024. All rights reserved.</p>
</footer>

</body>
</html>
```